Business Cards for Tomas and Welby

Design of business cards for two people with the recently created brand Caldor Mobile. Caldor Mobile wants to become a worldwide major player on the secondhand phone market. It gathers send hand phones from individuals, refurbish them and sell them throughout the world. It has a green impact (recycling) and we also contribute to social project in Africa (a percentage of our benefits are sent to build school, sport facilities, etc.

Target Market(s)

B2B - Tomas and Welby are in contact with distributors across Africa.

Industry/Entity Type

Wireless Communication

Contact Information for Business Card

Tomas Vireaux
Head of Emerging Markets
Caldor Energy South Africa (Pty) Ltd
Fennick Street 47
2031 Sandton - Johannesburg
South Africa
Tel: + 27 10 555 0184
Mobile : +27 82 55 017
Email : tomas.vireaux@caldormobile.example
Skype: tomas.vireaux
Web: www.caldormobile.example
 

Welby Crofts
Head of Southern Africa
Fennick Street 47
South Africa
Tel: + 27 10 555 0184
Mobile: +27 83 555 0297
Email: welby.crofts@caldormobile.example
Skype: welby.crofts
Web: www.caldormobile.example

Requirements
Must have
• The cards need to be "serious", trustable, with a worldwide presence.
Nice to have
• Some "green" / recycling touch would be nice but not necessary if in contradiction with the general design.

```html
<!DOCTYPE html>
<html lang="en">
<head>
<meta charset="utf-8">
<title>Caldor Mobile – Business Card</title>
<link href="https://fonts.googleapis.com/css2?family=Roboto:ital,wght@0,400;0,500;0,700;0,900;1,500&display=swap" rel="stylesheet">
<style>
  :root {
    --navy: #0b2c48;
    --navy-deep: #082740;
    --blue: #2b95d6;
    --pale: #e3edf6;
    --paper: #f7f8f9;
    --grey: #6d7277;
    --text: #3a3f44;
    --stage: #dfe2e5;
  }
  * { margin: 0; padding: 0; box-sizing: border-box; }
  html, body { width: 1200px; height: 886px; overflow: hidden; }
  body {
    background: var(--stage);
    font-family: "Roboto", Arial, sans-serif;
    position: relative;
  }
  .card {
    position: absolute;
    width: 560px;
    height: 320px;
    border-radius: 22px;
    overflow: hidden;
    box-shadow: 0 10px 28px rgba(0,0,0,.18);
  }

  /* Back */
  .card--back {
    left: 60px; top: 80px;
    background: var(--navy-deep);
  }
  .card--back .wordmark {
    position: absolute;
    left: 0; right: 0; top: 118px;
    display: flex; align-items: center; justify-content: center; gap: 14px;
    color: #fff;
    font-size: 40px; font-weight: 900; letter-spacing: -0.5px;
  }
  .wordmark .dot {
    width: 18px; height: 18px; border-radius: 50%;
    background: var(--blue);
  }
  .card--back .website {
    position: absolute;
    left: 0; right: 0; top: 196px;
    text-align: center;
    color: #fff;
    font-size: 13px; font-weight: 400; letter-spacing: 7px;
  }

  /* Front */
  .card--front {
    left: 580px; top: 486px;
    background: var(--paper);
    color: var(--text);
  }
  .card--front .corner-tint {
    position: absolute;
    right: 0; top: 0; width: 260px; height: 320px;
    background: linear-gradient(200deg, var(--pale) 0%, rgba(227,237,246,0.55) 55%, rgba(247,248,249,0) 100%);
  }
  .holder {
    position: absolute;
    right: 34px; top: 30px;
    text-align: right;
  }
  .holder .name {
    color: var(--navy);
    font-size: 17px; font-weight: 700; letter-spacing: 0.6px;
    text-transform: uppercase;
  }
  .holder .role {
    color: var(--blue);
    font-size: 14px; font-weight: 500; font-style: italic;
    margin-top: 2px;
  }
  .card--front .wordmark {
    position: absolute;
    left: 40px; top: 86px;
    display: flex; align-items: center; gap: 12px;
    color: var(--navy);
    font-size: 32px; font-weight: 900; letter-spacing: -0.4px;
  }
  .address {
    position: absolute;
    left: 40px; top: 146px;
    font-size: 12.5px; line-height: 16px;
    color: var(--grey);
  }
  .contact {
    position: absolute;
    left: 40px; top: 222px;
    font-size: 12.5px; line-height: 17px;
    color: var(--grey);
  }
  .contact b { color: var(--navy); font-weight: 700; margin-right: 4px; }
  .contact .strong { color: var(--text); font-weight: 700; letter-spacing: 0.3px; }
  .contact .gap { margin-left: 10px; }
  .contact .spacer { height: 8px; }
</style>
</head>
<body>

  <section class="card card--back" aria-label="Card back">
    <div class="wordmark"><span class="dot"></span>Caldor Mobile</div>
    <div class="website">www.caldormobile.example</div>
  </section>

  <section class="card card--front" aria-label="Card front">
    <div class="corner-tint"></div>

    <div class="holder">
      <div class="name">Tomas Vireaux</div>
      <div class="role">Head of Emerging Markets</div>
    </div>

    <div class="wordmark"><span class="dot"></span>Caldor Mobile</div>

    <div class="address">
      Caldor Energy South Africa (Pty) Ltd<br>
      Fennick Street 47, 2031 Sandton<br>
      Johannesburg<br>
      South Africa
    </div>

    <div class="contact">
      <div><b>P:</b>+ 27 10 555 0184<span class="gap"><b>C:</b>+27 82 55 017</span></div>
      <div><b>E:</b>tomas.vireaux@caldormobile.example</div>
      <div class="spacer"></div>
      <div><b>S:</b><span class="strong">tomas.vireaux</span></div>
      <div><b>W:</b><span class="strong">www.caldormobile.example</span></div>
    </div>
  </section>

</body>
</html>
```